LANDING PAGE on a Word Press platform.

I have a website, www.thecalmequityscout.com and need to create a new landing page. I purchased a new url, www.calmequityscout.com and set it up on Word Press. It has a theme (I was trying to do it myself, but gave up) but you can change it if you need to. I will give you access so you can work directly on the Word Press Platform. Please visit my site, www.thecalmequityscout, so you can see what we are selling.
Updates

Thank you for being so patient. Unfortunately I had some pressing personal problems and had to leave the country for a couple of weeks. I am back now and will choose a design today. Thank you again!

Target Market(s)

Stock Market, High Worth Individuals, Traders, Investors

Requirements
Must have
• My landing page must look very professional and rich. I am sending a copy of my logo but the "the" before The Calm Equity Scout, needs to be removed. Some testimonials and services we provide. (all found on my home page)
Nice to have
• I am open to a new color scheme if possible. The logo colors would have to be changed.
Should not have
• Should not be too busy with too many images or text. I want a clean and easy to read landing page

```html
<!DOCTYPE html>
<html lang="en">
<head>
<meta charset="utf-8">
<title>Calm Equity Scout</title>
<link rel="stylesheet" href="https://fonts.googleapis.com/css2?family=Open+Sans:wdth,wght@75..100,300..800&family=Oranienbaum&display=swap">
<style>
  :root {
    --gold: #c3960f;
    --gold-line: #d4a82a;
    --navy: #3a5a8c;
    --maroon: #8c3657;
    --green: #5a8f3b;
    --white: #ffffff;
    --ink: #222222;
    --grey-text: #6a6a6a;
    --rule: #d8d8d8;
    --sky-top: #5f6a92;
    --sky-bottom: #6d6a8f;
  }
  * { margin: 0; padding: 0; box-sizing: border-box; }
  html, body { width: 1200px; height: 900px; overflow: hidden; background: var(--white); }
  body { position: relative; font-family: "Open Sans", Arial, sans-serif; color: var(--ink); }

  .hero-scene {
    position: absolute; left: 0; top: 0; width: 1200px; height: 356px;
    background: linear-gradient(180deg, #7b84a8 0%, var(--sky-top) 40%, #4f5a80 62%, var(--sky-bottom) 100%);
  }

  .account-links { position: absolute; top: 7px; left: 892px; display: flex; gap: 9px; }
  .account-links a {
    display: block; height: 26px; line-height: 24px; padding: 0 12px;
    border: 1px solid var(--white); border-radius: 6px; color: var(--white);
    font-size: 11px; text-decoration: none; font-stretch: 85%;
  }

  .nav-band { position: absolute; left: 340px; top: 43px; width: 860px; height: 55px; background: var(--gold); }
  .main-nav { position: absolute; left: 483px; top: 43px; height: 55px; display: flex; }
  .main-nav a {
    display: block; position: relative; height: 55px; line-height: 55px; padding: 0 10px;
    color: var(--white); font-size: 12.5px; text-decoration: none; font-stretch: 85%;
    border-left: 1px solid var(--gold-line);
  }
  .main-nav a:first-child { padding: 0 14px 0 10px; }
  .main-nav a.current::after {
    content: ""; position: absolute; left: 50%; bottom: 1px; margin-left: -4px;
    border-left: 4px solid transparent; border-right: 4px solid transparent; border-bottom: 6px solid var(--white);
  }

  .brand { position: absolute; left: 169px; top: 31px; width: 214px; height: 76px; }
  .brand svg { position: absolute; left: 0; top: 0; }
  .brand-name {
    position: absolute; left: 52px; top: 16px; width: 130px;
    font-size: 19px; line-height: 21px; font-weight: 600; font-stretch: 80%; color: var(--gold);
  }

  .focus-tag {
    position: absolute; left: 792px; top: 175px; width: 152px; height: 108px;
    font-family: "Oranienbaum", Georgia, serif; color: var(--white); text-align: center;
  }
  .focus-tag .corner-top { position: absolute; left: 0; top: 0; width: 8px; height: 20px; border-left: 2px solid var(--white); border-top: 2px solid var(--white); }
  .focus-tag .corner-bottom { position: absolute; right: 2px; bottom: 0; width: 8px; height: 20px; border-right: 2px solid var(--white); border-bottom: 2px solid var(--white); }
  .focus-tag .line-small { display: block; font-size: 28px; line-height: 30px; margin-top: 4px; }
  .focus-tag .line-large { display: block; font-size: 40px; line-height: 36px; }

  .welcome-title {
    position: absolute; left: 169px; top: 261px; width: 512px; height: 95px;
    background: var(--gold); color: var(--white); padding: 28px 0 0 24px;
    font-size: 29px; font-weight: 300; white-space: nowrap;
  }
  .welcome-title strong { font-weight: 700; font-size: 36px; font-stretch: 75%; letter-spacing: -0.5px; margin-left: 8px; }

  .intro-letter {
    position: absolute; left: 169px; top: 356px; width: 512px; height: 255px;
    background: var(--navy); color: var(--white); padding: 27px 24px 0 24px;
  }
  .intro-letter .salutation { font-size: 14px; font-stretch: 90%; margin-bottom: 20px; }
  .intro-letter p.body { font-size: 11.6px; line-height: 20.5px; font-stretch: 88%; margin-bottom: 7px; }

  .portrait {
    position: absolute; left: 681px; top: 356px; width: 353px; height: 255px;
    background: linear-gradient(135deg, #e4e8ec 0%, #c9cfd6 45%, #8a8f99 70%, #3f4858 100%);
  }

  .subscribe-offer {
    position: absolute; left: 169px; top: 611px; width: 512px; height: 72px;
    background: var(--maroon); color: var(--white); padding: 0 24px; line-height: 72px;
    font-size: 16px; font-weight: 300; font-stretch: 88%; white-space: nowrap;
  }
  .subscribe-offer .emph { font-weight: 700; font-size: 21px; text-decoration: underline; text-underline-offset: 4px; }
  .subscribe-offer .price { font-weight: 700; font-size: 19px; margin-left: 4px; }

  .trial-offer {
    position: absolute; left: 681px; top: 611px; width: 353px; height: 72px;
    background: var(--green); color: var(--white); text-align: center; line-height: 72px;
    font-size: 16px; font-weight: 300; font-stretch: 88%; white-space: nowrap;
  }
  .trial-offer .emph { font-weight: 700; font-size: 21px; text-decoration: underline; text-underline-offset: 4px; margin-right: 4px; }

  .value-statement { position: absolute; left: 169px; top: 722px; width: 866px; text-align: center; font-family: "Oranienbaum", Georgia, serif; }
  .value-statement h2 { font-weight: 400; font-size: 19px; color: var(--ink); letter-spacing: 0.3px; }
  .value-statement p { margin: 10px auto 0; width: 600px; font-size: 19.5px; line-height: 23.5px; color: var(--grey-text); }

  .section-rule { position: absolute; left: 169px; top: 865px; width: 866px; height: 2px; background: var(--rule); }
</style>
</head>
<body>
  <div class="hero-scene" role="img" aria-label="City skyline across a river at dusk"></div>

  <div class="account-links">
    <a href="#">SUBSCRIBE</a>
    <a href="#">LOGIN</a>
  </div>

  <div class="nav-band"></div>
  <nav class="main-nav">
    <a class="current" href="#">Home</a>
    <a href="#">About</a>
    <a href="#">Current Portfolio</a>
    <a href="#">Latest Report</a>
    <a href="#">Watch List</a>
    <a href="#">Daily Ticker</a>
    <a href="#">Market News</a>
    <a href="#">Login</a>
  </nav>

  <div class="brand">
    <svg width="214" height="76" viewBox="0 0 214 76" aria-hidden="true">
      <polygon points="0,0 214,0 166,76 0,76" fill="#ffffff"/>
      <circle cx="30" cy="37" r="19" fill="#1f3f7a"/>
    </svg>
    <div class="brand-name">Calm Equity Scout</div>
  </div>

  <div class="focus-tag">
    <span class="corner-top"></span>
    <span class="line-small">STOCKS YOU</span>
    <span class="line-large">SHOULD</span>
    <span class="line-small">FOCUS ON</span>
    <span class="corner-bottom"></span>
  </div>

  <h1 class="welcome-title">Welcome To <strong>Calm Equity Scout</strong></h1>

  <section class="intro-letter">
    <p class="salutation">Dear Investor,</p>
    <p class="body">Our Team of Researchers, Stock Traders and Contributors would like to welcome you to "The Calm Equity Scout", an opportunity to receive research and opinions on companies and stocks that will outperform the market!!</p>
    <p class="body">If you are an investor or stock trader looking for high quality investment ideas with strong fundamentals to support them, look no further than the "The Calm Equity Scout" as an invaluable resource of investment information. Our approach combines fundamental and technical analysis in order to introduce fresh and successful ideas to our readers.</p>
  </section>

  <div class="portrait" role="img" aria-label="Portrait photo of a smiling senior advisor in a suit"></div>

  <div class="subscribe-offer">Become a paid <span class="emph">SUBSCRIBER</span> Monthly subscription <span class="price">$150.00</span></div>
  <div class="trial-offer"><span class="emph">TRY OUR FREE </span> 2 week trial Package!</div>

  <section class="value-statement">
    <h2>HIGH QUALITY INVESTMENT IDEAS WITH STRONG FUNDAMENTALS TO SUPPORT THEM</h2>
    <p>"TCES" is focused on individual stocks and sectors that have not been recommended by major research firms and allows our readers to take advantage of opportunities early on.</p>
  </section>

  <div class="section-rule"></div>
</body>
</html>
```